Personal Training Studio needs small flyer design

My Personal Training Studio is looking to offer local high end clothes shops the option to offer their customers free Personal Training at our studio. It will be a small flyer (more a slip - landscape) that can be put into customers shopping bags once they have purchased an item from the store.
It is being marketed as a Local Fitness Initiative which is called "Be Fit In Your Clothes" The idea is to come from a "Be Fit" health perspective but also "Fit into your clothes" from the clothes shops perspective. Perhaps the "Be" in a different colour to the rest of the title. I would like my company logo and colours to be used, plus the address of the of the studio (see website - www.harbourlane7strength.co.uk). Flyer can be double sided

Target Market(s)

High end clothing shops

Industry/Entity Type

Training

Requirements
Must have
• Reference to the fact that the voucher is offering a FREE Personal Training session. Contact us to book yours today.

```html
<!DOCTYPE html>
<html lang="en">
<head>
<meta charset="utf-8">
<title>Be Fit In Your Clothes – Harbour Lane 7 Strength</title>
<link href="https://fonts.googleapis.com/css2?family=Rubik+Dirt&family=PT+Sans:wght@400;700&family=Open+Sans:wght@700;800&family=Montserrat:wght@500&display=swap" rel="stylesheet">
<style>
  :root {
    --navy: #2b2f6b;
    --navy-deep: #262a63;
    --teal-band: #1d4d62;
    --grey-band: #7d8a92;
    --sky-light: #e3f0f6;
    --sky-mid: #b9d6e6;
    --footer-tint: rgba(128, 152, 172, 0.82);
    --circle-grey: #9aa0a3;
    --circle-navy: #3a3f78;
    --photo-neutral: #c3cfd7;
    --white: #ffffff;
  }
  html, body {
    margin: 0;
    padding: 0;
    overflow: hidden;
    background: #ffffff;
  }
  .flyer {
    position: relative;
    width: 1200px;
    height: 566px;
    overflow: hidden;
    background: linear-gradient(115deg, var(--sky-mid) 0%, var(--sky-light) 45%, #f4f9fc 75%, #eef4f7 100%);
  }
  .photo-athlete-left {
    position: absolute;
    left: 0; top: 0;
    width: 440px; height: 566px;
    background: linear-gradient(90deg, #7f9fb4 0%, #a9c4d4 55%, rgba(200, 222, 234, 0) 100%);
  }
  .decor-circles {
    position: absolute;
    left: 800px; top: 0;
    width: 400px; height: 431px;
  }
  .photo-athlete-right {
    position: absolute;
    left: 960px; top: 0;
    width: 175px; height: 431px;
    background: var(--photo-neutral);
    opacity: 0.85;
  }
  .headline {
    position: absolute;
    font-family: "Rubik Dirt", "Impact", sans-serif;
    line-height: 1;
    margin: 0;
    white-space: nowrap;
  }
  .headline-be {
    left: 266px; top: 2px;
    font-size: 150px;
    color: var(--navy);
    letter-spacing: -3px;
  }
  .headline-fit {
    left: 502px; top: 82px;
    font-size: 82px;
    color: var(--white);
  }
  .headline-clothes {
    left: 274px; top: 170px;
    font-size: 84px;
    color: var(--white);
  }
  .offer-free {
    position: absolute;
    left: 565px; top: 295px;
    width: 395px; height: 70px;
    background: linear-gradient(90deg, var(--teal-band) 0%, var(--teal-band) 88%, rgba(29, 77, 98, 0.2) 100%);
    display: flex;
    align-items: flex-end;
    font-family: "PT Sans", sans-serif;
    color: var(--white);
  }
  .offer-free .free-word {
    font-weight: 700;
    font-size: 74px;
    line-height: 0.9;
    margin-left: 6px;
    -webkit-text-stroke: 2px #173a4a;
    letter-spacing: 1px;
  }
  .offer-free .free-rest {
    font-size: 35px;
    margin-left: 12px;
    margin-bottom: 6px;
  }
  .offer-studio {
    position: absolute;
    left: 565px; top: 369px;
    width: 395px; height: 42px;
    background: linear-gradient(90deg, var(--grey-band) 0%, var(--grey-band) 88%, rgba(125, 138, 146, 0.1) 100%);
    font-family: "PT Sans", sans-serif;
    font-size: 34px;
    line-height: 42px;
    color: var(--white);
    padding-left: 2px;
    box-sizing: border-box;
  }
  .contact-band {
    position: absolute;
    left: 0; top: 431px;
    width: 820px; height: 135px;
    background: var(--footer-tint);
    font-family: "Open Sans", sans-serif;
    text-align: center;
  }
  .contact-band .phones {
    margin: 8px 0 0 0;
    font-size: 37px;
    font-weight: 800;
    color: var(--navy);
    letter-spacing: 0.5px;
  }
  .contact-band .address {
    margin: 0;
    font-size: 22px;
    font-weight: 700;
    color: var(--white);
  }
  .contact-band .website {
    margin: 0;
    font-size: 37px;
    font-weight: 800;
    color: var(--navy);
    line-height: 1.2;
  }
  .brand-panel {
    position: absolute;
    left: 820px; top: 431px;
    width: 380px; height: 135px;
    background: var(--navy-deep);
    display: flex;
    align-items: center;
    justify-content: center;
  }
  .brand-name {
    font-family: "Montserrat", sans-serif;
    font-weight: 500;
    font-size: 27px;
    line-height: 1.15;
    color: var(--white);
    letter-spacing: 2px;
    text-align: center;
    margin: 0;
  }
</style>
</head>
<body>
  <main class="flyer">
    <div class="photo-athlete-left" role="img" aria-label="Photo of a man lifting a dumbbell in a gym"></div>

    <svg class="decor-circles" viewBox="0 0 400 431" aria-hidden="true">
      <rect x="255" y="0" width="145" height="431" fill="#5a5f8f" opacity="0.35"/>
      <circle cx="125" cy="138" r="103" fill="var(--circle-grey)" opacity="0.75"/>
      <circle cx="300" cy="85" r="110" fill="var(--circle-navy)" opacity="0.85"/>
      <circle cx="310" cy="175" r="90" fill="var(--circle-navy)" opacity="0.7"/>
      <circle cx="340" cy="280" r="85" fill="var(--circle-grey)" opacity="0.8"/>
    </svg>

    <div class="photo-athlete-right" role="img" aria-label="Photo of a smiling woman in sportswear holding a small dumbbell"></div>

    <h1 class="headline headline-be">Be</h1>
    <p class="headline headline-fit">Fit In</p>
    <p class="headline headline-clothes">Your Clothes</p>

    <div class="offer-free"><span class="free-word">FREE</span><span class="free-rest">Personal</span></div>
    <div class="offer-studio">Training at our studio</div>

    <section class="contact-band">
      <p class="phones">07700 900318 • 01632 960481</p>
      <p class="address">7 Harbour Lane, Eastwick, North Yorkshire YO99 2ZZ</p>
      <p class="website">harbourlane7strength.co.uk</p>
    </section>

    <div class="brand-panel">
      <p class="brand-name">HARBOUR LANE 7<br>STRENGTH</p>
    </div>
  </main>
</body>
</html>
```